Computer consultant website

Plivet Software is a newly started computer consulting company. It's a small one-man company that provides mostly Kestrel applications but also websites in collaboration with designers. I'm running this company on the side of full time university studies.

I'm in need of a website which will function as:
Primarily - I'll direct potential clients to the page so they can read about the company, what i offer and past work.
Secondarily - Making my company visible through the web and maybe getting new clients.

The final design should look modern, clean and professional.

Pages that will be in the final website are (Note that it's not the exact titles as the page will not be in english):
* About
* Services (what Plivet offers)
* Portfolio/work
* Short news (like Framolines "News and press")
* Contact.

Inspiration
http://www.framoline.example/design/87836
http://www.quarnbelt.example/
http://www.framoline.example/design/845881
http://www.framoline.example/design/1369424 - Lighter design, however a bit cluttered.

No programming code is needed delivered at all. Focus on designing rather then coding.

If you have any questions, do not hesitate to send me a message.

Target Market(s)

Non-technical entrepreneurs and small companies.

Industry/Entity Type

University

Requirements
Must have
• Must have my company logo (see attachment).

Must in any way use both colors from my logo.

A way to logically rearrange content to fit smaller screens. I will implement this design so that it can be pleasantly viewed on mobile devices. You don't necessarily need to provide exactly how the design would look on mobile devices.

I need the following types of page designs:
* Landing page
* Content page
* Portfolio/work (with accompanying inside/clicked) page

Landing/start page must in any way include at least the information:
* Shorter version of "About Plivet"
* At least 1 most recent portfolio/work entry
* At least 1 most recent news entry
* Services that Plivet offers.
Nice to have
• -
Should not have
• Testimonials or newsletter.

```html
<!DOCTYPE html>
<html lang="en">
<head>
<meta charset="utf-8">
<title>Plivet Software</title>
<link rel="stylesheet" href="https://fonts.googleapis.com/css2?family=Oswald:wght@400;500&family=Questrial&display=swap">
<style>
:root{
  --blue:#2a7bf2;
  --green:#9ccc1e;
  --ink:#333333;
  --band:#333333;
  --muted:#6b6b6b;
  --soft:#8a8a8a;
  --line:#d4d4d4;
  --paper:#ffffff;
  --fog:#e4e4e4;
}
*{margin:0;padding:0;box-sizing:border-box}
html,body{width:1120px;height:1200px;overflow:hidden}
body{
  position:relative;
  font-family:"Questrial",sans-serif;
  color:var(--ink);
  background:
    linear-gradient(to bottom,var(--paper) 0,var(--paper) 838px,#ececec 838px,#d6d6d6 1126px,var(--paper) 1126px);
}
.hero-glow{position:absolute;left:0;top:0;width:1120px;height:680px;
  background:radial-gradient(ellipse at 50% 40%,#ffffff 45%,#ededed 100%)}
.nav{position:absolute;top:30px;left:0;width:1120px;display:flex;justify-content:center;font-size:12.5px;text-transform:uppercase;color:#555}
.nav a{color:inherit;text-decoration:none;padding:5px 14px;border-left:1px dotted #ccc;line-height:16px}
.nav a:first-of-type{border-left:none}
.nav a.current{color:var(--blue);border:2.5px solid var(--blue);border-radius:6px;padding:4px 9px;margin-right:6px}
.nav a.current + a{border-left:none}
.brand{position:absolute;top:86px;left:0;width:1120px;display:flex;justify-content:center;align-items:center;gap:12px}
.brand-dot{width:48px;height:48px;border-radius:50%;background:var(--blue)}
.brand-name{font-family:"Questrial",sans-serif;font-size:50px;color:var(--ink);line-height:1;letter-spacing:-1px}
.hero-art{position:absolute;left:340px;top:156px;width:452px;height:448px;border-radius:6px;
  background:linear-gradient(135deg,#4a4a4a 0,#5d7fb4 50%,#8fc23a 100%);opacity:.85}
.headline{position:absolute;top:614px;left:0;width:1120px;text-align:center;font-family:"Oswald",sans-serif;font-weight:500;font-size:44px;letter-spacing:-1.5px;text-transform:uppercase;line-height:1;transform:scaleX(.86)}
.headline .green{color:var(--green)}
.headline .blue{color:var(--blue)}
.headline .dark{color:var(--ink)}
.services{position:absolute;top:680px;left:0;width:1120px;height:158px;background:var(--band)}
.service{position:absolute;top:20px;width:240px;text-align:center;color:#686868;font-size:13.5px;letter-spacing:.3px;text-transform:uppercase}
.service svg{display:block;margin:0 auto 12px;height:56px}
.service.web{left:195px}
.service.app{left:422px}
.service.resp{left:658px}
.service-divider{position:absolute;top:30px;width:0;height:80px;border-left:1px dotted #555}
.card{position:absolute;top:808px;height:194px;background:var(--paper);border:1px solid #ddd;box-shadow:0 1px 2px rgba(0,0,0,.08)}
.card.work{left:242px;width:316px}
.card.news{left:568px;width:317px}
.card-title{position:absolute;left:13px;top:16px;font-family:"Oswald",sans-serif;font-weight:400;font-size:22px;letter-spacing:-.8px;text-transform:uppercase;transform-origin:left;transform:scaleX(.9)}
.work .card-title{color:var(--blue)}
.news .card-title{color:var(--ink)}
.card-mark{position:absolute;right:15px;top:12px;width:26px;height:26px;border-radius:50%;border:4px solid #d6d6d6}
.card-rule{position:absolute;left:13px;right:13px;top:50px;border-top:1px solid #e6e6e6}
.entry-title{position:absolute;top:60px;font-family:"Oswald",sans-serif;font-size:19px;letter-spacing:-.6px;text-transform:uppercase;transform-origin:left;transform:scaleX(.85);white-space:nowrap}
.work .entry-title{left:147px;color:var(--blue)}
.news .entry-title{left:61px;color:var(--ink)}
.entry-text{position:absolute;top:88px;font-size:9px;line-height:11px;color:var(--soft)}
.work .entry-text{left:147px;width:152px}
.news .entry-text{left:61px;width:236px}
.work-thumb{position:absolute;left:10px;top:52px;width:130px;height:130px;border-radius:4px;background:linear-gradient(160deg,#3c7fd0 0,#bcd3ee 55%,#e8e8e8 75%,#f7f7f7 100%)}
.date{position:absolute;left:13px;top:60px;width:36px;height:38px;background:var(--blue);color:#fff;text-align:center;border-radius:2px}
.date .day{display:block;font-family:"Oswald",sans-serif;font-size:17px;line-height:20px}
.date .month{display:block;font-size:9.5px;line-height:11px}
.btn{position:absolute;bottom:0;height:28px;padding:0 11px;color:#fff;font-family:"Oswald",sans-serif;font-size:15px;line-height:28px;text-transform:uppercase;border-radius:4px 4px 0 0}
.work .btn{left:207px;background:var(--blue)}
.news .btn{left:58px;background:#2b2b2b}
.welcome{position:absolute;top:1036px;left:238px;font-family:"Oswald",sans-serif;font-weight:500;font-size:42px;letter-spacing:-1.5px;color:#3a3a3a;text-transform:uppercase;line-height:1;transform-origin:left;transform:scaleX(.82)}
.welcome-divider{position:absolute;top:1040px;left:398px;height:48px;border-left:1px dotted #999}
.welcome-text{position:absolute;top:1039px;left:414px;width:472px;font-size:9px;line-height:11.5px;color:var(--muted)}
.footer-rule{position:absolute;top:1126px;left:0;width:1120px;border-top:1px solid #cfcfcf}
.copyright{position:absolute;top:1160px;left:242px;font-size:9px;color:var(--soft)}
.social{position:absolute;top:1160px;left:517px;display:flex;gap:7px}
.social span{width:11px;height:11px;border-radius:50%;background:#b5b5b5}
.footer-brand{position:absolute;top:1144px;left:777px;display:flex;align-items:center;gap:8px}
.footer-brand .brand-dot{width:34px;height:34px;background:#c2c2c2}
.footer-brand .brand-name{font-size:32px;color:#a8a8a8}
</style>
</head>
<body>
<div class="hero-glow"></div>

<nav class="nav">
  <a class="current" href="#">About</a>
  <a href="#">Our Services</a>
  <a href="#">Our Portfolio</a>
  <a href="#">News and Press</a>
  <a href="#">Contact Us</a>
</nav>

<div class="brand">
  <span class="brand-dot"></span>
  <span class="brand-name">plivet</span>
</div>

<div class="hero-art" role="img" aria-label="Hero illustration: a smartphone showing colourful app icons with a green robot beside it"></div>

<h1 class="headline"><span class="green">Kestrel</span> <span class="blue">and Responsive</span> <span class="dark">Web Delvelopment</span></h1>

<section class="services">
  <div class="service web">
    <svg viewBox="0 0 70 56"><rect x="7" y="4" width="56" height="40" rx="2" fill="none" stroke="#686868" stroke-width="4"/><rect x="0" y="46" width="70" height="5" rx="2" fill="#686868"/><circle cx="35" cy="22" r="7" fill="none" stroke="#686868" stroke-width="2.5"/><rect x="32" y="29" width="6" height="6" fill="#686868"/></svg>
    Website Design
  </div>
  <div class="service-divider" style="left:419px"></div>
  <div class="service app">
    <svg viewBox="0 0 48 56"><rect x="4" y="6" width="40" height="46" rx="8" fill="#686868"/></svg>
    Kestrel Applications
  </div>
  <div class="service-divider" style="left:661px"></div>
  <div class="service resp">
    <svg viewBox="0 0 44 56"><rect x="3" y="2" width="38" height="52" rx="4" fill="none" stroke="#686868" stroke-width="4"/></svg>
    Responsive Development
  </div>
</section>

<article class="card work">
  <h2 class="card-title">Recent Work</h2>
  <span class="card-mark"></span>
  <div class="card-rule"></div>
  <div class="work-thumb" role="img" aria-label="Photo of a desktop computer showing a recent project"></div>
  <h3 class="entry-title">Kestrel Development</h3>
  <p class="entry-text">We build fast, tidy mobile apps for small firms, from first sketch to store release, with clear updates along the way and support after launch.</p>
  <a class="btn">Readmore</a>
</article>

<article class="card news">
  <h2 class="card-title">Latest News</h2>
  <span class="card-mark"></span>
  <div class="card-rule"></div>
  <div class="date"><span class="day">06</span><span class="month">March</span></div>
  <h3 class="entry-title">Responsive Web Designing</h3>
  <p class="entry-text">Our new site layouts adapt to every screen size, so your visitors get a clean and easy view on phones, tablets and desktops alike, with no extra work needed from you.</p>
  <a class="btn">Readmore</a>
</article>

<h2 class="welcome">Welcome</h2>
<div class="welcome-divider"></div>
<p class="welcome-text">Plivet Software is a small consulting studio that builds mobile apps and websites for entrepreneurs and small companies. We keep things simple, explain each step in plain words and deliver clean work on time, whether you need a new app, a fresh site or help improving what you already have. Get in touch to talk about your next project.</p>

<div class="footer-rule"></div>
<p class="copyright">© 2013 | Plivet. All rights reserved</p>
<div class="social"><span></span><span></span><span></span><span></span><span></span></div>
<div class="footer-brand">
  <span class="brand-dot"></span>
  <span class="brand-name">plivet</span>
</div>
</body>
</html>
```